New Word Template Design Project

Dellvane needs a modern and fresh corporate word template (*.dotm). We are a technology integrator the operates in the ICT sector in Portugal and Spain. Our solutions and services are detailed here: dellvane-example.com.
This word template should have mainly Dellvane's blue tones, and among other purposes, it's meant to be the basis of our commercial proposals. As such, in the cover page we need to place info such as: project name, client name, Dellvane reference, client reference, date and document type (the latter with less visual emphasis).
Our official font is Raleway and we are also sending our Brand Manual where the official company colors are specified.
Concerning the components of the document, we would like to have an index, 5 headings levels, 5 bullet points levels, 2 table styles and the other components that are part of the document we are also sending.

Target Market(s)

Executives and IT Directors

Industry/Entity Type

Information Technology

Font styles to use
Other font styles liked:
• Raleway

Colors
249fd3

Requirements
Must have
• Not jeopardizing the designers creativity, we would like it to be aligned with our website image.
• Respect brand colors (mostly the blue ones) and font
• Cover page info: project name, client name, Dellvane reference, client reference, date and document type
• 5 levels of headings considering a report
• 5 levels of bullet points
• 2 layouts for tables
• index
Nice to have
• A professional corporate template, yet conveying some modern, dynamic and "fresh" image.
Should not have
• Too many colors
• An unprofessional image

```html
<!DOCTYPE html>
<html lang="en">
<head>
<meta charset="utf-8">
<title>Dellvane Word Template – Pages</title>
<link href="https://fonts.googleapis.com/css2?family=Raleway:ital,wght@0,400;0,500;0,600;0,700;0,800;0,900;1,500&display=swap" rel="stylesheet">
<style>
:root{
  --blue:#249fd3;
  --blue-light:#d3e1f2;
  --blue-head:#5b86c4;
  --ink:#111111;
  --stage:#3b3b3b;
  --board:#c3c3c3;
  --paper:#ffffff;
  --grey-text:#222;
}
*{box-sizing:border-box;margin:0;padding:0}
html,body{width:1200px;height:3141px;overflow:hidden}
body{background:var(--board);font-family:'Raleway',sans-serif;color:var(--ink);position:relative}
.stage{position:absolute;left:0;top:0;width:1200px;height:744px;background:var(--stage)}
.stage .page{left:355px;top:26px}
.label{position:absolute;width:490px;text-align:center;font-size:23px;font-weight:600;letter-spacing:.5px;color:#222}
.page{position:absolute;width:490px;height:691px;background:var(--paper);box-shadow:0 2px 4px rgba(0,0,0,.2);overflow:hidden}
.cover svg{display:block}
/* inner header */
.page-head .rule{position:absolute;left:0;top:46px;width:345px;height:2px;background:var(--blue)}
.brand{position:absolute;left:356px;top:30px;display:flex;align-items:center;gap:8px}
.brand .dot{width:22px;height:22px;border-radius:50%;background:var(--blue)}
.brand .name{font-size:20px;font-weight:500;color:var(--grey-text)}
/* inner footer */
.page-foot{position:absolute;left:0;bottom:6px;width:490px;height:28px;background:var(--ink)}
.page-foot .url{position:absolute;left:25px;top:7px;font-size:11.5px;letter-spacing:3px;color:#fff;font-weight:500}
.page-foot .num{position:absolute;right:0;top:-8px;width:80px;height:36px;background:var(--blue);clip-path:polygon(22% 0,100% 0,100% 100%,0 100%);color:#fff;font-weight:700;font-size:14px;line-height:36px;text-align:center;padding-left:14px}
/* index */
.index-title{position:absolute;top:126px;width:100%;text-align:center;font-size:23px;font-weight:700}
.index-row{position:absolute;left:63px;width:370px;font-size:14px;display:flex;align-items:center}
.index-row .entry{width:102px}
.index-row .leader{flex:1;border-bottom:1.5px dashed #444;margin:0 30px 0 0;height:0}
/* heading levels */
.lvl-tab{position:absolute;left:0;width:48px;background:var(--blue);border-radius:0 12px 12px 0;color:#fff;font-weight:700;text-align:center}
.h1{position:absolute;left:64px;top:147px;line-height:26px;font-size:19px;font-weight:500;letter-spacing:.2px}
.h1 .dots{color:var(--blue);letter-spacing:4px;margin-left:6px;font-weight:900}
.h2{position:absolute;left:137px;top:222px;width:284px;height:30px;border-radius:15px;background:var(--blue);color:#fff;font-size:17px;font-weight:500;text-align:center;line-height:30px}
.h3{position:absolute;left:143px;top:320px;width:280px;height:28px}
.h3 .stripe{position:absolute;top:0;width:6px;height:28px;background:var(--blue);transform:skewX(-25deg)}
.h3 .bar{position:absolute;left:27px;top:0;width:225px;height:28px;background:var(--blue);color:#fff;font-size:14.5px;font-weight:500;text-align:center;line-height:28px}
.h4-bar{position:absolute;left:175px;top:404px;width:245px;height:28px;background:var(--blue);color:#fff;font-size:14.5px;font-style:italic;font-weight:500;line-height:28px;padding-left:32px}
.icon-badge{position:absolute;border-radius:50%;background:#fff;border:2px solid var(--blue);display:flex;align-items:center;justify-content:center}
.icon-badge i{display:block;width:12px;height:16px;background:repeating-linear-gradient(#333 0 2px,#fff 2px 4px);border:2px solid #333}
.h5{position:absolute;left:180px;top:487px;width:200px;height:56px;background:var(--blue);color:#fff;font-size:13.5px;font-weight:700;line-height:16px;padding:13px 12px}
.h5::after{content:"";position:absolute;left:22px;bottom:-12px;border-left:12px solid transparent;border-right:4px solid transparent;border-top:12px solid var(--blue)}
.h5 .q{position:absolute;right:10px;top:6px;font-size:38px;line-height:40px;color:#7fd0f2;font-weight:500}
/* bullets */
.b1{position:absolute;left:25px;font-size:13.5px;font-weight:500;display:flex;align-items:center;gap:10px}
.b1::before{content:"";width:7px;height:7px;border-radius:50%;background:var(--blue)}
.b2{position:absolute;display:flex;gap:4px;height:18px}
.b2 .n{width:18px;background:var(--blue);color:#fff;font-size:10px;text-align:center;line-height:18px;font-weight:600}
.b2 .t{width:178px;background:var(--blue);color:#fff;font-size:12px;line-height:18px;padding-left:7px;font-weight:500}
.b3{position:absolute;font-size:12px;font-style:italic;font-weight:500;display:flex;align-items:center;gap:7px}
.b3 svg{width:10px;height:10px}
.b4{position:absolute;height:38px;width:240px}
.b4 .icon-badge{left:0;top:0;width:38px;height:38px;z-index:1}
.b4 .rib{position:absolute;left:22px;top:8px;width:200px;height:22px;background:var(--blue);clip-path:polygon(0 0,100% 0,94% 50%,100% 100%,0 100%);color:#fff;font-size:10px;line-height:22px;padding-left:30px;font-weight:500}
.b5{position:absolute;font-size:8.8px;font-weight:500;display:flex;align-items:center;gap:6px}
.b5::before{content:"";width:4px;height:4px;border-right:1.5px solid var(--blue);border-top:1.5px solid var(--blue);transform:rotate(45deg)}
/* tables */
.table-title{position:absolute;width:100%;text-align:center;font-size:15px;font-weight:500}
.doc-table{position:absolute;left:24px;width:441px;border-collapse:collapse;font-size:8.6px;text-align:center;border:1px solid #888}
.doc-table th{height:22px;font-size:10px;font-weight:500;border-left:1px solid #fff}
.doc-table td{height:23.2px;border-left:1px solid #888}
.t1 th{background:var(--blue-head);color:#fff}
.t1 tbody tr:nth-child(odd) td{background:var(--blue-light)}
.t1 td{border-left-color:#fff}
.t2 th{background:#fff;color:var(--blue);border-bottom:1px solid #888;border-left:1px solid #888}
.t2 tbody tr:nth-child(even) td{background:var(--blue-light)}
.brand-lockup{position:absolute;left:700px;top:2615px;display:flex;align-items:center;gap:18px}
.brand-lockup .dot{width:70px;height:70px;border-radius:50%;background:var(--blue)}
.brand-lockup .name{font-size:58px;font-weight:500;color:var(--grey-text)}
</style>
</head>
<body>

<section class="stage">
  <article class="page cover">
    <svg width="490" height="691" viewBox="0 0 490 691">
      <defs><linearGradient id="ph" x1="0" y1="0" x2="1" y2="1"><stop offset="0" stop-color="#8c99a6"/><stop offset=".5" stop-color="#3f5267"/><stop offset="1" stop-color="#26313d"/></linearGradient></defs>
      <rect width="490" height="320" fill="url(#ph)" role="img" aria-label="Photo of an engineer watching monitoring screens in a network operations centre"/>
      <path d="M0,250 L0,340 C15,420 40,470 70,450 C95,420 110,340 160,322 L330,318 C390,312 440,300 490,290 L490,250 Z" fill="#161616"/>
      <path d="M0,691 L0,340 C15,420 40,470 70,450 C95,420 110,340 160,322 L330,318 C390,312 440,300 490,290 L490,691 Z" fill="#fff"/>
      <path d="M0,300 C10,420 40,480 72,458 C100,430 110,350 160,330 L330,326 C390,318 440,302 490,292" fill="none" stroke="#249fd3" stroke-width="16"/>
      <circle cx="251" cy="342" r="96" fill="#fff" stroke="#249fd3" stroke-width="5"/>
      <text x="251" y="352" text-anchor="middle" font-family="Raleway,sans-serif" font-size="30" font-weight="500" fill="#222">dellvane</text>
      <text x="245" y="515" text-anchor="middle" font-family="Raleway,sans-serif" font-size="66" font-weight="900" fill="#111">PROJECT</text>
      <text x="245" y="575" text-anchor="middle" font-family="Raleway,sans-serif" font-size="66" font-weight="900" fill="#249fd3">NAME</text>
      <text x="245" y="605" text-anchor="middle" font-family="Raleway,sans-serif" font-size="13" font-weight="800" fill="#111">CLIENT NAME</text>
      <rect x="0" y="649" width="490" height="42" fill="#111"/>
      <polygon points="288,640 490,640 490,691 268,691" fill="#249fd3"/>
      <text x="24" y="674" font-family="Raleway,sans-serif" font-size="9" font-weight="800" fill="#fff">DELLVANE REFERENCE  |  CLIENT REFERENCE</text>
      <text x="386" y="672" text-anchor="middle" font-family="Raleway,sans-serif" font-size="16" font-weight="800" fill="#fff">22nd October 2019</text>
    </svg>
  </article>
</section>

<h2 class="label" style="left:108px;top:827px">COVER PAGE</h2>
<h2 class="label" style="left:616px;top:827px">INNER PAGE 1</h2>

<article class="page cover" style="left:108px;top:870px">
  <svg width="490" height="691" viewBox="0 0 490 691">
    <defs><linearGradient id="ph2" x1="0" y1="0" x2="1" y2="1"><stop offset="0" stop-color="#8c99a6"/><stop offset=".5" stop-color="#3f5267"/><stop offset="1" stop-color="#26313d"/></linearGradient></defs>
    <rect width="490" height="320" fill="url(#ph2)" role="img" aria-label="Photo of an engineer watching monitoring screens in a network operations centre"/>
    <path d="M0,250 L0,340 C15,420 40,470 70,450 C95,420 110,340 160,322 L330,318 C390,312 440,300 490,290 L490,250 Z" fill="#161616"/>
    <path d="M0,691 L0,340 C15,420 40,470 70,450 C95,420 110,340 160,322 L330,318 C390,312 440,300 490,290 L490,691 Z" fill="#fff"/>
    <path d="M0,300 C10,420 40,480 72,458 C100,430 110,350 160,330 L330,326 C390,318 440,302 490,292" fill="none" stroke="#249fd3" stroke-width="16"/>
    <circle cx="251" cy="342" r="96" fill="#fff" stroke="#249fd3" stroke-width="5"/>
    <text x="251" y="352" text-anchor="middle" font-family="Raleway,sans-serif" font-size="30" font-weight="500" fill="#222">dellvane</text>
    <text x="245" y="515" text-anchor="middle" font-family="Raleway,sans-serif" font-size="66" font-weight="900" fill="#111">PROJECT</text>
    <text x="245" y="575" text-anchor="middle" font-family="Raleway,sans-serif" font-size="66" font-weight="900" fill="#249fd3">NAME</text>
    <text x="245" y="605" text-anchor="middle" font-family="Raleway,sans-serif" font-size="13" font-weight="800" fill="#111">CLIENT NAME</text>
    <rect x="0" y="649" width="490" height="42" fill="#111"/>
    <polygon points="288,640 490,640 490,691 268,691" fill="#249fd3"/>
    <text x="24" y="674" font-family="Raleway,sans-serif" font-size="9" font-weight="800" fill="#fff">DELLVANE REFERENCE  |  CLIENT REFERENCE</text>
    <text x="386" y="672" text-anchor="middle" font-family="Raleway,sans-serif" font-size="16" font-weight="800" fill="#fff">22nd October 2019</text>
  </svg>
</article>

<article class="page index-page" style="left:616px;top:870px">
  <header class="page-head"><div class="rule"></div><div class="brand"><span class="dot"></span><span class="name">dellvane</span></div></header>
  <h1 class="index-title">INDEX</h1>
  <div class="index-row" style="top:188px"><span class="entry">Heading</span><span class="leader"></span><span>3</span></div>
  <div class="index-row" style="top:219px"><span class="entry">Bullet Point</span><span class="leader"></span><span>4</span></div>
  <div class="index-row" style="top:249px"><span class="entry">Table</span><span class="leader"></span><span>5</span></div>
  <footer class="page-foot"><span class="url">www.dellvane-example.com</span><span class="num">2</span></footer>
</article>

<article class="page headings-page" style="left:108px;top:1583px">
  <header class="page-head"><div class="rule"></div><div class="brand"><span class="dot"></span><span class="name">dellvane</span></div></header>
  <div class="lvl-tab" style="top:147px;height:26px;line-height:26px;font-size:15px">1</div>
  <h1 class="h1">LOREM IPSUM IS A SIMPLY TEXT<span class="dots">••••</span></h1>
  <div class="lvl-tab" style="top:225px;height:24px;line-height:24px;font-size:14px">2</div>
  <h2 class="h2">Lorem ipsum is a simply text</h2>
  <div class="lvl-tab" style="top:323px;height:22px;line-height:22px;font-size:13px">3</div>
  <h3 class="h3"><span class="stripe" style="left:6px"></span><span class="stripe" style="left:16px"></span><span class="bar">Lorem ipsum is a simply text</span><span class="stripe" style="left:260px"></span><span class="stripe" style="left:270px"></span></h3>
  <div class="lvl-tab" style="top:408px;height:20px;line-height:20px;font-size:12px">4</div>
  <h4 class="h4-bar">Lorem ipsum is a simply text</h4>
  <div class="icon-badge" style="left:148px;top:398px;width:42px;height:42px"><i></i></div>
  <div class="lvl-tab" style="top:515px;height:18px;line-height:18px;font-size:11px">5</div>
  <h5 class="h5">Lorem ipsum is a simply<br>dummy text<span class="q">?</span></h5>
  <footer class="page-foot"><span class="url">www.dellvane-example.com</span><span class="num">3</span></footer>
</article>

<article class="page bullets-page" style="left:616px;top:1583px">
  <header class="page-head"><div class="rule"></div><div class="brand"><span class="dot"></span><span class="name">dellvane</span></div></header>
  <p class="b1" style="top:86px">Lorem ipsum is a simply text</p>
  <p class="b1" style="top:111px">Lorem ipsum is a simply text</p>
  <p class="b1" style="top:135px">Lorem ipsum is a simply text</p>

  <p class="b2" style="left:25px;top:194px"><span class="n">1</span><span class="t">Lorem ipsum is a simply text</span></p>
  <p class="b2" style="left:25px;top:224px"><span class="n">2</span><span class="t">Lorem ipsum is a simply text</span></p>
  <p class="b2" style="left:25px;top:253px"><span class="n">3</span><span class="t">Lorem ipsum is a simply text</span></p>
  <p class="b2" style="left:263px;top:194px"><span class="n">4</span><span class="t">Lorem ipsum is a simply text</span></p>
  <p class="b2" style="left:263px;top:224px"><span class="n">5</span><span class="t">Lorem ipsum is a simply text</span></p>
  <p class="b2" style="left:263px;top:253px"><span class="n">6</span><span class="t">Lorem ipsum is a simply text</span></p>

  <p class="b3" style="left:25px;top:309px"><svg viewBox="0 0 10 10"><circle cx="5" cy="5" r="4.3" fill="none" stroke="#249fd3"/><path d="M3 5l1.5 1.5L7 3.5" fill="none" stroke="#249fd3"/></svg>Lorem ipsum is a simply text</p>
  <p class="b3" style="left:25px;top:332px"><svg viewBox="0 0 10 10"><circle cx="5" cy="5" r="4.3" fill="none" stroke="#249fd3"/><path d="M3 5l1.5 1.5L7 3.5" fill="none" stroke="#249fd3"/></svg>Lorem ipsum is a simply text</p>
  <p class="b3" style="left:25px;top:355px"><svg viewBox="0 0 10 10"><circle cx="5" cy="5" r="4.3" fill="none" stroke="#249fd3"/><path d="M3 5l1.5 1.5L7 3.5" fill="none" stroke="#249fd3"/></svg>Lorem ipsum is a simply text</p>
  <p class="b3" style="left:255px;top:309px"><svg viewBox="0 0 10 10"><circle cx="5" cy="5" r="4.3" fill="none" stroke="#249fd3"/><path d="M3 5l1.5 1.5L7 3.5" fill="none" stroke="#249fd3"/></svg>Lorem ipsum is a simply text</p>
  <p class="b3" style="left:255px;top:332px"><svg viewBox="0 0 10 10"><circle cx="5" cy="5" r="4.3" fill="none" stroke="#249fd3"/><path d="M3 5l1.5 1.5L7 3.5" fill="none" stroke="#249fd3"/></svg>Lorem ipsum is a simply text</p>
  <p class="b3" style="left:255px;top:355px"><svg viewBox="0 0 10 10"><circle cx="5" cy="5" r="4.3" fill="none" stroke="#249fd3"/><path d="M3 5l1.5 1.5L7 3.5" fill="none" stroke="#249fd3"/></svg>Lorem ipsum is a simply text</p>

  <div class="b4" style="left:23px;top:408px"><span class="icon-badge"><i></i></span><span class="rib">Lorem ipsum is a simply text</span></div>
  <div class="b4" style="left:51px;top:450px"><span class="icon-badge"><i></i></span><span class="rib">Lorem ipsum is a simply text</span></div>
  <div class="b4" style="left:78px;top:492px"><span class="icon-badge"><i></i></span><span class="rib">Lorem ipsum is a simply text</span></div>

  <p class="b5" style="left:25px;top:564px">Lorem ipsum is a simply text</p>
  <p class="b5" style="left:25px;top:582px">Lorem ipsum is a simply text</p>
  <p class="b5" style="left:25px;top:600px">Lorem ipsum is a simply text</p>
  <p class="b5" style="left:178px;top:564px">Lorem ipsum is a simply text</p>
  <p class="b5" style="left:178px;top:582px">Lorem ipsum is a simply text</p>
  <p class="b5" style="left:178px;top:600px">Lorem ipsum is a simply text</p>
  <p class="b5" style="left:333px;top:564px">Lorem ipsum is a simply text</p>
  <p class="b5" style="left:333px;top:582px">Lorem ipsum is a simply text</p>
  <p class="b5" style="left:333px;top:600px">Lorem ipsum is a simply text</p>
  <footer class="page-foot"><span class="url">www.dellvane-example.com</span><span class="num">4</span></footer>
</article>

<h2 class="label" style="left:108px;top:2306px">INNER PAGE 2</h2>
<h2 class="label" style="left:616px;top:2306px">INNER PAGE 3</h2>

<article class="page tables-page" style="left:108px;top:2363px">
  <header class="page-head"><div class="rule"></div><div class="brand"><span class="dot"></span><span class="name">dellvane</span></div></header>
  <h3 class="table-title" style="top:112px">TABLE - 1</h3>
  <table class="doc-table t1" style="top:140px">
    <thead><tr><th>TITLE HERE</th><th>TITLE HERE</th><th>TITLE HERE</th><th>TITLE HERE</th></tr></thead>
    <tbody>
      <tr><td>Lorem ipsum</td><td>Lorem ipsum</td><td>Lorem ipsum</td><td>Lorem ipsum</td></tr>
      <tr><td>Lorem ipsum</td><td>Lorem ipsum</td><td>Lorem ipsum</td><td>Lorem ipsum</td></tr>
      <tr><td>Lorem ipsum</td><td>Lorem ipsum</td><td>Lorem ipsum</td><td>Lorem ipsum</td></tr>
      <tr><td>Lorem ipsum</td><td>Lorem ipsum</td><td>Lorem ipsum</td><td>Lorem ipsum</td></tr>
      <tr><td>Lorem ipsum</td><td>Lorem ipsum</td><td>Lorem ipsum</td><td>Lorem ipsum</td></tr>
      <tr><td>Lorem ipsum</td><td>Lorem ipsum</td><td>Lorem ipsum</td><td>Lorem ipsum</td></tr>
      <tr><td>Lorem ipsum</td><td>Lorem ipsum</td><td>Lorem ipsum</td><td>Lorem ipsum</td></tr>
    </tbody>
  </table>
  <h3 class="table-title" style="top:371px">TABLE - 2</h3>
  <table class="doc-table t2" style="top:400px">
    <thead><tr><th>TITLE HERE</th><th>TITLE HERE</th><th>TITLE HERE</th><th>TITLE HERE</th></tr></thead>
    <tbody>
      <tr><td>Lorem ipsum</td><td>Lorem ipsum</td><td>Lorem ipsum</td><td>Lorem ipsum</td></tr>
      <tr><td>Lorem ipsum</td><td>Lorem ipsum</td><td>Lorem ipsum</td><td>Lorem ipsum</td></tr>
      <tr><td>Lorem ipsum</td><td>Lorem ipsum</td><td>Lorem ipsum</td><td>Lorem ipsum</td></tr>
      <tr><td>Lorem ipsum</td><td>Lorem ipsum</td><td>Lorem ipsum</td><td>Lorem ipsum</td></tr>
      <tr><td>Lorem ipsum</td><td>Lorem ipsum</td><td>Lorem ipsum</td><td>Lorem ipsum</td></tr>
      <tr><td>Lorem ipsum</td><td>Lorem ipsum</td><td>Lorem ipsum</td><td>Lorem ipsum</td></tr>
      <tr><td>Lorem ipsum</td><td>Lorem ipsum</td><td>Lorem ipsum</td><td>Lorem ipsum</td></tr>
    </tbody>
  </table>
  <footer class="page-foot"><span class="url">www.dellvane-example.com</span><span class="num">5</span></footer>
</article>

<div class="brand-lockup"><span class="dot"></span><span class="name">dellvane</span></div>

<h2 class="label" style="left:108px;top:3085px">INNER PAGE 4</h2>

</body>
</html>
```